I'm looking for a fresh new design for my business Leonard Fasque Creative.
I am a photographer and videographer.
The card must be easy to print, eye catching and easy to read. It must reflect the fact that I work in a creative area, but not so edgy as to scare away my corporate clients.
Sub text should read Photography, Video, Design
There also needs to be room for phone number and email.

```html
<!DOCTYPE html>
<html lang="en">
<head>
<meta charset="UTF-8">
<title>Leonard Fasque Creative — Business Card</title>
<link href="https://fonts.googleapis.com/css2?family=Arimo:wght@400&family=Josefin+Sans:wght@300;400&display=swap" rel="stylesheet">
<style>
  :root {
    --page-bg: #3a2f2a;
    --card-black: #0c0c0c;
    --card-glow: #3a3a3a;
    --band-black: #070707;
    --accent-red: #9b1c1c;
    --text-white: #f2f2f2;
    --text-grey: #9a9a9a;
    --contact-grey: #d0d0d0;
    --photo-light: #8a8a8a;
    --photo-mid: #4d4d4d;
    --photo-dark: #1e1e1e;
  }
  * { box-sizing: border-box; margin: 0; padding: 0; }
  html, body {
    width: 1200px; height: 1000px; overflow: hidden;
    background: var(--page-bg);
  }
  .sheet {
    width: 1200px; height: 1000px;
    display: flex; flex-direction: column; align-items: center; justify-content: center;
    gap: 60px;
  }
  .card {
    width: 740px; height: 400px;
    position: relative; overflow: hidden;
    box-shadow: 0 12px 30px rgba(0,0,0,0.45);
  }

  /* Front */
  .card-front {
    background: radial-gradient(ellipse 55% 60% at 50% 48%, var(--card-glow) 0%, #1a1a1a 45%, var(--card-black) 100%);
    display: flex; flex-direction: column; align-items: center; justify-content: center;
    gap: 10px;
  }
  .name-row {
    display: flex; align-items: center; gap: 14px;
  }
  .name-square {
    width: 10px; height: 10px;
    background: var(--accent-red);
    flex: none;
  }
  .brand-name {
    font-family: "Arimo", Arial, sans-serif;
    font-weight: 400;
    font-size: 34px; letter-spacing: 1px;
    color: var(--text-white); line-height: 1.1;
  }
  .brand-services {
    font-family: "Arimo", Arial, sans-serif;
    font-weight: 400;
    font-size: 12px; letter-spacing: 2px;
    color: var(--text-grey); text-transform: uppercase;
  }

  /* Back */
  .card-back {
    background: radial-gradient(ellipse 50% 40% at 50% 68%, #2a2a2a 0%, var(--card-black) 100%);
  }
  .top-band {
    height: 84px; background: var(--band-black);
  }
  .photo-strip {
    display: flex; height: 182px;
  }
  .photo {
    flex: 1; border-right: 2px solid var(--band-black);
  }
  .photo:last-child { border-right: none; }
  .photo-street { background: linear-gradient(135deg, var(--photo-dark), var(--photo-light) 60%, var(--photo-mid)); }
  .photo-busker { background: linear-gradient(180deg, var(--photo-mid), var(--photo-light) 55%, var(--photo-mid)); }
  .photo-dog { background: linear-gradient(160deg, var(--photo-light), var(--photo-mid) 65%, var(--photo-dark)); }
  .contact-line {
    position: absolute; left: 0; right: 0; bottom: 70px;
    text-align: center;
    font-family: "Josefin Sans", Arial, sans-serif; font-weight: 300;
    font-size: 15px; letter-spacing: 1.2px;
    color: var(--contact-grey);
  }
  .contact-line span + span { margin-left: 16px; }
</style>
</head>
<body>
<main class="sheet">
  <section class="card card-front">
    <div class="name-row">
      <span class="name-square"></span>
      <h1 class="brand-name">Leonard Fasque Creative</h1>
    </div>
    <p class="brand-services">Photography, Video, Design</p>
  </section>

  <section class="card card-back">
    <div class="top-band"></div>
    <div class="photo-strip">
      <div class="photo photo-street" role="img" aria-label="Black and white street photograph of a group of young people gathered on a sidewalk"></div>
      <div class="photo photo-busker" role="img" aria-label="Black and white photograph of a woman walking past a street guitarist by a shop window"></div>
      <div class="photo photo-dog" role="img" aria-label="Black and white photograph of a fluffy dog sitting beside framed sketches on a street"></div>
    </div>
    <p class="contact-line">
      <span>(345)-555-0142</span><span>leonard.fasque@fasquemail.com</span><span>@leonard.fasque</span>
    </p>
  </section>
</main>
</body>
</html>
```